Carpentry and Building Business Card

I'm looking for a business card that is minimalistic and that incorporates the theme of my Velmor logo.
On one side I'd like the VELMOR logo with my details on the other side.
Double sided with curved edges

Target Market(s)

Construction / renovation
Adults

Industry/Entity Type

Tradesman

Contact Information for Business Card

Logo on one side, details on the other

Colors

Designer to choose only greyscale colors for use in the design.

Requirements
Must have
• Nilo Petrakis
VELMOR CONSTRUCT
Carpentry & Building Services
0481236574
Velmorconstruct@brixmail.com
Lic No. 718263D
Nice to have
• Fb and insta icons. @velmorconstruct
Should not have
• No hammer or tool icons please.

No address line.

```html
<!DOCTYPE html>
<html lang="en">
<head>
<meta charset="utf-8">
<title>Velmor Construct – Business Card</title>
<link rel="stylesheet" href="https://fonts.googleapis.com/css2?family=Poppins:wght@400;500;600&display=swap">
<style>
  :root {
    --backdrop: #2b2b2b;
    --card-black: #161616;
    --accent-grey: #b8b8b8;
    --ink-dark: #1a1a1a;
    --text-light: #ffffff;
  }
  * { box-sizing: border-box; margin: 0; padding: 0; }
  html, body {
    width: 1200px;
    height: 1082px;
    overflow: hidden;
    background: var(--backdrop);
    font-family: "Poppins", sans-serif;
  }
  .canvas {
    position: relative;
    width: 1200px;
    height: 1082px;
    display: flex;
    flex-direction: column;
    align-items: center;
    justify-content: center;
    gap: 56px;
  }
  .card {
    position: relative;
    width: 760px;
    height: 434px;
    border-radius: 34px;
    overflow: hidden;
    display: flex;
    background: var(--card-black);
    box-shadow: 0 14px 30px rgba(0,0,0,0.45);
  }
  .card__panel {
    width: 36%;
    background: var(--accent-grey);
    display: flex;
    align-items: center;
    justify-content: center;
  }
  .card__body {
    flex: 1;
    display: flex;
    align-items: center;
  }

  /* Details side */
  .brand-name {
    font-weight: 500;
    font-size: 34px;
    letter-spacing: 0;
    color: var(--ink-dark);
  }
  .details {
    padding-left: 56px;
    color: var(--text-light);
  }
  .details__name {
    font-weight: 600;
    font-size: 24px;
    line-height: 1.2;
  }
  .details__company {
    font-weight: 600;
    font-size: 24px;
    line-height: 1.3;
    margin-top: 8px;
    padding-bottom: 12px;
    border-bottom: 2px solid var(--accent-grey);
    width: 400px;
  }
  .details__tagline {
    font-size: 17px;
    margin-top: 14px;
  }
  .contact-list {
    list-style: none;
    margin-top: 10px;
  }
  .contact-list__item {
    display: flex;
    align-items: center;
    gap: 12px;
    font-size: 17px;
    line-height: 1.75;
  }
  .contact-list__icon {
    width: 18px;
    height: 18px;
    flex-shrink: 0;
    stroke: var(--accent-grey);
    fill: none;
    stroke-width: 1.6;
    stroke-linecap: round;
    stroke-linejoin: round;
  }

  /* Brand side */
  .brand-title {
    padding-left: 60px;
    font-weight: 500;
    font-size: 64px;
    letter-spacing: 0;
    color: var(--text-light);
  }
</style>
</head>
<body>
<main class="canvas">

  <section class="card card--details" aria-label="Business card, details side">
    <div class="card__panel">
      <p class="brand-name">VELMOR</p>
    </div>
    <div class="card__body">
      <div class="details">
        <p class="details__name">Nilo Petrakis</p>
        <p class="details__company">VELMOR CONSTRUCT</p>
        <p class="details__tagline">Carpentry &amp; Building Services</p>
        <ul class="contact-list">
          <li class="contact-list__item">
            <svg class="contact-list__icon" viewBox="0 0 24 24" aria-hidden="true"><path d="M5 3h4l2 5-2.5 1.5a11 11 0 0 0 6 6L16 13l5 2v4a2 2 0 0 1-2 2A17 17 0 0 1 3 5a2 2 0 0 1 2-2z"/></svg>
            0481236574
          </li>
          <li class="contact-list__item">
            <svg class="contact-list__icon" viewBox="0 0 24 24" aria-hidden="true"><rect x="3" y="5" width="18" height="14" rx="1"/><path d="M3 6l9 7 9-7"/></svg>
            Velmorconstruct@brixmail.com
          </li>
          <li class="contact-list__item">
            <svg class="contact-list__icon" viewBox="0 0 24 24" aria-hidden="true"><circle cx="12" cy="8" r="4"/><path d="M4 21a8 8 0 0 1 16 0"/></svg>
            Lic No. 718263D
          </li>
        </ul>
      </div>
    </div>
  </section>

  <section class="card card--brand" aria-label="Business card, brand side">
    <div class="card__panel"></div>
    <div class="card__body">
      <p class="brand-title">VELMOR</p>
    </div>
  </section>

</main>
</body>
</html>
```